Voucher design for Willow Brook Spa

1) Create a creative design and voucher for Willow Brook Spa that create a lasting memory for the audience. I would like to give out vouchers to all neighbours.
2) Kindly look at the website www.willowbrookspa-example.com
3) Content must include logo, address, telephone number and website.

Here is the content of the voucher

2) 15 dollar cash voucher - off full body massage
3) 10 dollars cash voucher - off foot massage
(Both the fully body massage and foot massage, slimming massage vouchers must be separated and separate vouchers and independent)
4) 20 dollars cash voucher - off slimming massage

Terms and conditions at the back of the voucher
1) Willow Brook Spa reserved the right to amend change the terms and conditions without prior notice.
2) This promotional is not valid with any other promotions existing. e.g
3) Each person is entitled to use one voucher at any one time.

Target Market(s)

Mass market

Font styles to use
Decorative

Requirements
Must have
• 1) Creatives cash vouchers and beautiful design
• 2) Logo fo the company
• 3) Address and telephone number
• 4) website
• 5) Terms and conditions
Nice to have
• You can use tree or lotus as the symbol but it must be toward nature, beautiful, eye catching and creative.

```html
<!DOCTYPE html>
<html lang="en">
<head>
<meta charset="utf-8">
<title>Willow Brook Spa – Foot Massage Cash Voucher</title>
<link href="https://fonts.googleapis.com/css2?family=Marcellus&family=Arimo:ital,wght@0,400;1,400;1,700&display=swap" rel="stylesheet">
<style>
  :root{
    --page:#d9d9d9;
    --forest:#1f5a2e;
    --deep-green:#23532c;
    --lime:#8fd14f;
    --white:#ffffff;
    --blue:#2e6fa8;
    --teal:#2c9a93;
    --green:#4fae4a;
    --gold:#c9a25a;
    --gold-dark:#7a5426;
  }
  html,body{margin:0;padding:0;width:1200px;height:1200px;overflow:hidden;background:var(--page);}
  .canvas{position:relative;width:1200px;height:1200px;}
  .voucher{
    position:absolute;left:50px;top:343px;width:1285px;height:600px;
    transform:scale(0.856);transform-origin:0 0;overflow:hidden;
    box-shadow:0 10px 24px rgba(0,0,0,.25);
  }
  .voucher-art{position:absolute;inset:0;width:1285px;height:600px;}
  .brand-badge{
    position:absolute;left:45px;top:25px;width:160px;height:160px;border-radius:50%;
    background:var(--white);border:5px solid var(--forest);box-sizing:border-box;
    display:flex;align-items:center;justify-content:center;text-align:center;
  }
  .brand-name{font-family:"Marcellus",serif;color:var(--forest);font-size:21px;line-height:1.15;}
  .title-cash{position:absolute;left:318px;top:58px;font-family:"Marcellus",serif;font-size:50px;color:var(--deep-green);}
  .title-voucher{position:absolute;left:340px;top:118px;font-family:"Marcellus",serif;font-size:96px;color:var(--deep-green);letter-spacing:4px;line-height:1;}
  .title-voucher .initial{font-size:132px;}
  .service{position:absolute;left:500px;top:240px;width:270px;text-align:center;font-family:"Arimo",sans-serif;font-style:italic;font-size:38px;color:var(--white);}
  .value{position:absolute;left:970px;top:70px;width:240px;height:240px;text-align:center;color:var(--lime);font-family:"Arimo",sans-serif;}
  .value-currency{display:block;margin-top:28px;font-size:58px;line-height:1;}
  .value-amount{display:block;font-style:italic;font-weight:700;font-size:104px;line-height:1;}
  .contact{position:absolute;left:700px;top:422px;width:360px;text-align:center;font-family:"Arimo",sans-serif;font-size:22px;line-height:28px;color:var(--white);}
  .contact p{margin:0;}
</style>
</head>
<body>
<div class="canvas">
  <div class="voucher">
    <svg class="voucher-art" viewBox="0 0 1285 600" xmlns="http://www.w3.org/2000/svg">
      <defs>
        <linearGradient id="base" x1="0" y1="0" x2="0.3" y2="1">
          <stop offset="0" stop-color="#2f5f9e"/>
          <stop offset="0.45" stop-color="#2c8f86"/>
          <stop offset="1" stop-color="#3f9a3a"/>
        </linearGradient>
        <linearGradient id="wave" x1="0" y1="0" x2="1" y2="1">
          <stop offset="0" stop-color="#4fa0c8"/>
          <stop offset="0.5" stop-color="#3aa7a0"/>
          <stop offset="1" stop-color="#5bbf79"/>
        </linearGradient>
        <linearGradient id="photo" x1="0" y1="0" x2="1" y2="1">
          <stop offset="0" stop-color="#f3e6da"/>
          <stop offset="0.5" stop-color="#e9c9b6"/>
          <stop offset="1" stop-color="#f2dde0"/>
        </linearGradient>
        <linearGradient id="gold" x1="0" y1="0" x2="1" y2="0">
          <stop offset="0" stop-color="#7a5426"/>
          <stop offset="0.4" stop-color="#e8cf8d"/>
          <stop offset="1" stop-color="#8a6330"/>
        </linearGradient>
      </defs>
      <rect width="1285" height="600" fill="url(#base)"/>
      <path d="M0 600 L0 420 C300 560 700 330 1285 330 L1285 600 Z" fill="url(#wave)" opacity="0.75"/>
      <path d="M0 600 L0 470 C250 590 500 450 900 600 Z" fill="#3c9a3c" opacity="0.7"/>
      <path d="M290 0 C180 120 60 330 140 430 C220 520 420 420 700 370 C950 330 1150 320 1285 350 L1285 0 Z"
            fill="url(#photo)" role="img" aria-label="Photo of hands giving a foot massage beside pink lotus flowers and white towels"/>
      <path d="M290 0 C180 120 60 330 140 430 C220 520 420 420 700 370 C950 330 1150 320 1285 350"
            fill="none" stroke="url(#gold)" stroke-width="14"/>
      <path d="M275 0 C160 120 40 340 130 445 C220 540 430 440 700 388 C950 345 1150 338 1285 368"
            fill="none" stroke="#5e3a1a" stroke-width="4" opacity="0.7"/>
      <line x1="470" y1="92" x2="910" y2="92" stroke="#ffffff" stroke-width="2"/>
      <path d="M345 260 L455 260 L463 270 M910 260 L800 260 L792 270" fill="none" stroke="#ffffff" stroke-width="2"/>
      <circle cx="1090" cy="190" r="140" fill="none" stroke="#3c6a3c" stroke-width="3"/>
      <circle cx="1090" cy="190" r="120" fill="var(--deep-green)"/>
    </svg>

    <div class="brand-badge"><span class="brand-name">Willow Brook<br>Spa</span></div>

    <div class="title-cash">Cash</div>
    <div class="title-voucher"><span class="initial">V</span>OUCHER</div>
    <div class="service">foot massage</div>

    <div class="value">
      <span class="value-currency">$</span>
      <span class="value-amount">10</span>
    </div>

    <div class="contact">
      <p>27 Harbour Lane #02-14</p>
      <p>Singapore - 430127</p>
      <p>+65 6100 2345</p>
      <p>www.willowbrookspa-example.com</p>
    </div>
  </div>
</div>
</body>
</html>
```